Letterhead Design Project

I would like some modern, youthful, yet professional.

Industry/Entity Type

It Professional

Requirements
Must have
• On the left side the names of the Planning Committee:
Planning Committee
Founding Leaders:
Dorvin Ashcombe, BOLT Youths - Washington, DC
Marisol Pennock, BOLT Youths - Washington, DC
Odessaline Gribble, BOLT Youths - Washington, DC
Terrence Wolcott, BOLT Youths - Washington, DC
Bree Tuller, Alliance of Coastal Pines Youth In Care Circle
Vesna Doluchova, Alliance of Coastal Pnies Youth in Care Circle
Rosalind Pike, Northstar Youth In Care Circle, Canada
Ilse Brook Tovah, Northstar Youth In Care Circle, Canada
Chair
Jonelle Birch, BOLT Youths, Washington, DC
Co-Chairs
Paul Whitcombe, Global Kinship Guardians Union, Amsterdam. Netherlands
Myra Tolliver, Bright Pathways Partners, Jackson, MS
Gordon Fenwick, Wilma R Thornbury Trust

```html
<!DOCTYPE html>
<html lang="en">
<head>
<meta charset="utf-8">
<title>Letterhead – 2012 Worldwide Assembly of Young Voices</title>
<link rel="stylesheet" href="https://fonts.googleapis.com/css2?family=Oswald:wght@300;400;500&display=swap">
<style>
  :root {
    --blue-deep: #0a2f74;
    --blue-mid: #114a9e;
    --blue-bright: #2a78cf;
    --blue-glow: #4d9be6;
    --ink-light: #ffffff;
    --ink-soft: #cfe2fb;
    --paper: #ffffff;
  }
  * { margin: 0; padding: 0; box-sizing: border-box; }
  html, body { width: 900px; height: 1200px; overflow: hidden; background: var(--paper); }
  .letterhead {
    position: relative;
    width: 900px;
    height: 1200px;
    background: var(--paper);
    font-family: "Oswald", "Arial Narrow", sans-serif;
    overflow: hidden;
  }
  .band { position: absolute; left: 0; width: 900px; }
  .band--top { top: 0; height: 520px; }
  .band--bottom { bottom: 0; height: 260px; }

  .committee {
    position: absolute;
    color: var(--ink-light);
    font-size: 13.5px;
    line-height: 21px;
    font-weight: 300;
    letter-spacing: 0.1px;
  }
  .committee--planning { left: 24px; top: 14px; }
  .committee--chairs { left: 490px; top: 14px; }
  .committee__heading { font-weight: 400; }
  .committee__name { font-weight: 500; }

  .brand {
    position: absolute;
    left: 618px;
    top: 188px;
    width: 260px;
    text-align: center;
    color: var(--ink-soft);
  }
  .brand__mark {
    width: 86px;
    height: 86px;
    margin: 0 auto 10px;
    border-radius: 50%;
    background: var(--blue-glow);
  }
  .brand__name {
    font-weight: 300;
    font-size: 21px;
    line-height: 24px;
    letter-spacing: 0.5px;
    text-transform: uppercase;
  }
</style>
</head>
<body>
<div class="letterhead">
  <svg class="band band--top" viewBox="0 0 900 520" aria-hidden="true">
    <defs>
      <radialGradient id="topGlow" cx="0.75" cy="0.45" r="0.8">
        <stop offset="0" stop-color="var(--blue-bright)"/>
        <stop offset="0.55" stop-color="var(--blue-mid)"/>
        <stop offset="1" stop-color="var(--blue-deep)"/>
      </radialGradient>
    </defs>
    <path d="M0 0 H900 V470 C760 420 520 360 0 282 Z" fill="var(--blue-glow)" opacity="0.55"/>
    <path d="M0 0 H900 V455 C760 405 520 345 0 272 Z" fill="url(#topGlow)"/>
  </svg>

  <svg class="band band--bottom" viewBox="0 0 900 260" aria-hidden="true">
    <defs>
      <linearGradient id="bottomGlow" x1="0" y1="1" x2="1" y2="0">
        <stop offset="0" stop-color="var(--blue-deep)"/>
        <stop offset="0.6" stop-color="var(--blue-mid)"/>
        <stop offset="1" stop-color="var(--blue-bright)"/>
      </linearGradient>
    </defs>
    <path d="M250 260 C470 160 700 90 900 40 V260 Z" fill="var(--blue-glow)" opacity="0.5"/>
    <path d="M275 260 C490 170 710 105 900 58 V260 Z" fill="url(#bottomGlow)"/>
  </svg>

  <div class="committee committee--planning">
    <p class="committee__heading">Planning Committee</p>
    <p class="committee__heading">Founding Leaders</p>
    <p><span class="committee__name">Dorvin Ashcombe</span> BOLT Youths - Washington, DC</p>
    <p><span class="committee__name">Marisol Pennock</span> BOLT Youths - Washington, DC</p>
    <p><span class="committee__name">Odessaline Gribble</span> BOLT Youths - Washington, DC</p>
    <p><span class="committee__name">Terrence Wolcott</span> BOLT Youths - Washington, DC</p>
    <p><span class="committee__name">Bree Tuller</span> Alliance of Coastal Pines Youth In Care Circle</p>
    <p><span class="committee__name">Vesna Doluchova</span> Alliance of Coastal Pnies Youth in Care Circle</p>
    <p><span class="committee__name">Rosalind Pike</span> Northstar Youth In Care Circle, Canada</p>
    <p><span class="committee__name">Ilse Brook Tovah</span> Northstar Youth In Care Circle, Canada</p>
  </div>

  <div class="committee committee--chairs">
    <p class="committee__heading">Chair</p>
    <p><span class="committee__name">Jonelle Birch</span> BOLT Youths, Washington, DC</p>
    <p class="committee__heading">Co-Chairs</p>
    <p><span class="committee__name">Paul Whitcombe</span> Global Kinship Guardians Union, Amsterdam, Netherlands</p>
    <p><span class="committee__name">Myra Tolliver</span> Bright Pathways Partners, Jackson, MS</p>
    <p><span class="committee__name">Gordon Fenwick</span> Wilma R Thornbury Trust</p>
  </div>

  <div class="brand">
    <div class="brand__mark"></div>
    <p class="brand__name">2012 Worldwide Assembly<br>of Young Voices</p>
  </div>
</div>
</body>
</html>
```